Christmas Banner for frontpage of website

New online scarf store just opened needs a Christmas Banner stating Free Delivery (UK only). Also if it could incorporate guaranteed Christmas delivery if ordered before 18th (might be too wordy though?) I would really like it to bring some colour to the page. The page is currently black and white with a pink accent and is very simple which is why I would like something modern and elegant, simple but with some colour. It is a shopify store I understand the banner size should be 950px by 290px the website is www.velmorrow.co.uk

Target Market(s)

Ladies

Industry/Entity Type

Store

Requirements
Should not have
• Not to look tacky.

```html
<!DOCTYPE html>
<html lang="en">
<head>
<meta charset="UTF-8">
<title>Velmorrow – Christmas Free Delivery Banner</title>
<link rel="stylesheet" href="https://fonts.googleapis.com/css2?family=Archivo:wght@700&family=Chewy&display=block">
<style>
  :root {
    --page-bg: #ffffff;
    --festive-red: #e8140f;
    --bauble-red: #d9221c;
    --bauble-dark: #9e100c;
    --badge-red: #9a0f0c;
    --frost-white: #f6f5f4;
    --frost-blue: #bcd3e2;
    --ink-shadow: rgba(40, 30, 30, 0.55);
  }

  * { margin: 0; padding: 0; box-sizing: border-box; }

  html, body {
    width: 1200px;
    height: 1000px;
    overflow: hidden;
    background: var(--page-bg);
  }

  .christmas-banner {
    position: absolute;
    left: 125px;
    top: 355px;
    width: 950px;
    height: 290px;
    overflow: hidden;
    background: var(--frost-white);
  }

  .banner-backdrop {
    position: absolute;
    inset: 0;
    background:
      radial-gradient(ellipse 130px 110px at 740px 20px, rgba(205, 40, 35, 0.55), transparent 70%),
      radial-gradient(ellipse 200px 170px at 640px 160px, rgba(170, 200, 222, 0.75), transparent 70%),
      radial-gradient(ellipse 170px 200px at 900px 130px, rgba(150, 185, 210, 0.8), transparent 72%),
      radial-gradient(ellipse 160px 140px at 500px 90px, rgba(232, 224, 222, 0.9), transparent 70%),
      radial-gradient(ellipse 220px 90px at 640px 290px, rgba(205, 190, 180, 0.45), transparent 70%),
      linear-gradient(90deg, #f2f1f0 0%, var(--frost-white) 50%, #e3ebf0 100%);
  }

  .bauble-photo {
    position: absolute;
    left: -170px;
    top: -190px;
    width: 540px;
    height: 620px;
    border-radius: 50%;
    background:
      radial-gradient(ellipse 60% 55% at 55% 48%, rgba(240, 225, 225, 0.35), transparent 70%),
      radial-gradient(ellipse at 62% 40%, #ef3a32 0%, var(--bauble-red) 40%, var(--bauble-dark) 100%);
    box-shadow: 0 0 12px 4px rgba(200, 60, 55, 0.35);
  }

  .free-delivery {
    position: absolute;
    left: 520px;
    top: 61px;
    font-family: "Archivo", "Arial", sans-serif;
    font-weight: 700;
    font-size: 33px;
    letter-spacing: 0.3px;
    color: var(--festive-red);
    text-shadow: 2px 3px 2px var(--ink-shadow);
    line-height: 1;
  }

  .gift-badge {
    position: absolute;
    left: 822px;
    top: 33px;
    width: 92px;
    height: 92px;
    border-radius: 50%;
    background: radial-gradient(circle at 60% 55%, #efe6c8 0 28%, var(--badge-red) 30%);
  }

  .christmas-guarantee {
    position: absolute;
    right: 44px;
    top: 188px;
    text-align: right;
    font-family: "Chewy", "Trebuchet MS", sans-serif;
    font-weight: 400;
    font-size: 30px;
    line-height: 37px;
    color: var(--festive-red);
    text-shadow:
      -2px -2px 0 #fff, 2px -2px 0 #fff, -2px 2px 0 #fff, 2px 2px 0 #fff,
      0 -2px 0 #fff, 0 2px 0 #fff, -2px 0 0 #fff, 2px 0 0 #fff,
      3px 4px 3px var(--ink-shadow);
  }
</style>
</head>
<body>
  <section class="christmas-banner" aria-label="Velmorrow Christmas free delivery banner">
    <div class="banner-backdrop" role="img" aria-label="Soft blurred white, red and pale blue Christmas ornaments in the background"></div>
    <div class="bauble-photo" role="img" aria-label="Close-up of a red Christmas bauble decorated with a glittering white snowflake and a red jewel"></div>

    <h1 class="free-delivery">FREE DELIVERY</h1>

    <div class="gift-badge" role="img" aria-label="Round red badge with a wrapped gift box and stars"></div>

    <p class="christmas-guarantee">Guaranteed Christmas delivery<br>if ordered before 18th</p>
  </section>
</body>
</html>
```